Vintage "Greetings from Door County" Design for Wall

I are looking to recreate the vintage "Greetings from" postcard graphic from the 1940-50s. The main focus will be the saying "Greetings from Door County". Door County is a resort area in Wisconsin and we will use this graphic as a backdrop for tourist's instagram pictures. The letters of "Door County" will include things that the area is known for such as swimming, fishing, beaches, boating, biking, camping, cherry orchards, sunsets on the water etc. I have attached an actual postcard from the 50s for Door County to help you visualize the project (Picture 1). I have also attached landmarks and iconic features of Door County to include in the letters (Pictures 2-10). I want it to be more whimsical in nature with drawings to depict these landmarks as opposed to actual realistic pictures (Example 1 & 2). Please ask any questions to help clarify the project. Thanks and good luck!
Target Market(s)
Tourists
Industry/Entity Type
Retail
Colors
Designer to choose colors to be used in the design.
Look and feel

```html
<!DOCTYPE html>
<html lang="en">
<head>
<meta charset="utf-8">
<title>Greetings from Door County, Wisconsin</title>
<link rel="stylesheet" href="https://fonts.googleapis.com/css2?family=Damion&family=Rubik+Mono+One&family=Yellowtail&display=swap">
<style>
  :root {
    --page: #ffffff;
    --card-cream: #f0e9cf;
    --card-edge: #d9cfa8;
    --ink-navy: #15132b;
    --side-navy: #1c1a3a;
    --outline-violet: #4a4fb0;
    --extrude-red: #5a1416;
    --script-grey: #a8a8b0;
    --sky-top: #6b3a22;
    --sky-mid: #d9782a;
    --horizon: #f2a23a;
    --water: #7a4a2a;
    --foliage: #23241a;
  }
  * { margin: 0; padding: 0; box-sizing: border-box; }
  html, body { width: 1200px; height: 857px; overflow: hidden; background: var(--page); }
  .postcard { display: block; width: 1200px; height: 857px; }
  .block-letters { font-family: "Rubik Mono One", "Arial Black", sans-serif; }
  .script {
    font-family: "Yellowtail", "Damion", cursive;
    fill: var(--ink-navy);
    stroke: var(--script-grey);
    stroke-width: 3;
    paint-order: stroke fill;
  }
  .extrude-deep { fill: var(--extrude-red); stroke: var(--extrude-red); stroke-width: 4; stroke-linejoin: round; }
  .extrude-side { fill: var(--side-navy); stroke: var(--side-navy); stroke-width: 4; stroke-linejoin: round; }
  .letter-outline { fill: none; stroke: var(--outline-violet); stroke-width: 8; stroke-linejoin: round; }
  .letter-edge { fill: none; stroke: var(--ink-navy); stroke-width: 3; stroke-linejoin: round; }
</style>
</head>
<body>
<svg class="postcard" viewBox="0 0 1200 857" xmlns="http://www.w3.org/2000/svg" xmlns:xlink="http://www.w3.org/1999/xlink">
  <defs>
    <linearGradient id="sunset-sky" x1="0" y1="0" x2="0" y2="1">
      <stop offset="0" stop-color="var(--sky-top)"/>
      <stop offset="0.3" stop-color="var(--sky-mid)"/>
      <stop offset="0.58" stop-color="var(--horizon)"/>
      <stop offset="0.64" stop-color="#b5602a"/>
      <stop offset="0.8" stop-color="var(--water)"/>
      <stop offset="1" stop-color="var(--foliage)"/>
    </linearGradient>
    <radialGradient id="sun-glow" cx="0.5" cy="0.5" r="0.5">
      <stop offset="0" stop-color="#fff3b0"/>
      <stop offset="0.3" stop-color="#ffc552" stop-opacity="0.8"/>
      <stop offset="1" stop-color="#f2a23a" stop-opacity="0"/>
    </radialGradient>
    <linearGradient id="fill-bluff" x1="0" y1="0" x2="0" y2="1"><stop offset="0" stop-color="#7f8a2e"/><stop offset="1" stop-color="#a9752e"/></linearGradient>
    <linearGradient id="fill-ferry" x1="0" y1="0" x2="0" y2="1"><stop offset="0" stop-color="#5fa0d0"/><stop offset="0.5" stop-color="#e8eef2"/><stop offset="1" stop-color="#1c2030"/></linearGradient>
    <linearGradient id="fill-barn" x1="0" y1="0" x2="0" y2="1"><stop offset="0" stop-color="#6aa7c9"/><stop offset="0.45" stop-color="#7a4a36"/><stop offset="1" stop-color="#8c8676"/></linearGradient>
    <linearGradient id="fill-autumn" x1="0" y1="0" x2="0" y2="1"><stop offset="0" stop-color="#c2551f"/><stop offset="0.6" stop-color="#7d3a1c"/><stop offset="1" stop-color="#3b6ec0"/></linearGradient>
    <linearGradient id="fill-sign" x1="0" y1="0" x2="0" y2="1"><stop offset="0" stop-color="#4a8a78"/><stop offset="0.5" stop-color="#c9d3d8"/><stop offset="1" stop-color="#3d5a6a"/></linearGradient>
    <linearGradient id="fill-cherry" x1="0" y1="0" x2="0" y2="1"><stop offset="0" stop-color="#b2262e"/><stop offset="1" stop-color="#7a1420"/></linearGradient>
    <linearGradient id="fill-fire" x1="0" y1="0" x2="0" y2="1"><stop offset="0" stop-color="#e5a02a"/><stop offset="0.5" stop-color="#d2461c"/><stop offset="1" stop-color="#6a1e12"/></linearGradient>
    <linearGradient id="fill-shore" x1="0" y1="0" x2="0" y2="1"><stop offset="0" stop-color="#3a7ab0"/><stop offset="0.4" stop-color="#5a4a30"/><stop offset="1" stop-color="#3c5a3a"/></linearGradient>
    <linearGradient id="fill-tower" x1="0" y1="0" x2="0" y2="1"><stop offset="0" stop-color="#4a9ad8"/><stop offset="1" stop-color="#2a4a3a"/></linearGradient>
    <linearGradient id="fill-lighthouse" x1="0" y1="0" x2="0" y2="1"><stop offset="0" stop-color="#3e86c0"/><stop offset="0.5" stop-color="#2f4a30"/><stop offset="1" stop-color="#7a2a1e"/></linearGradient>

    <text id="door-shape" class="block-letters" x="236" y="362" font-size="235" textLength="735" lengthAdjust="spacingAndGlyphs">DOOR</text>
    <text id="county-shape" class="block-letters" x="108" y="612" font-size="230" textLength="1010" lengthAdjust="spacingAndGlyphs">COUNTY</text>
  </defs>

  <rect class="card-stock" x="14" y="18" width="1172" height="824" rx="26" fill="var(--card-cream)" stroke="var(--card-edge)" stroke-width="3"/>

  <g class="sunset-scene" role="img" aria-label="Photograph of a sunset over the bay with clouds and dark treetops in the foreground">
    <rect x="46" y="44" width="1108" height="764" rx="16" fill="url(#sunset-sky)"/>
    <ellipse cx="552" cy="402" rx="90" ry="60" fill="url(#sun-glow)"/>
  </g>

  <g class="headline-block" role="group" aria-label="Door County">
    <g class="word-door" transform="rotate(2 600 300)">
      <g class="extrusion">
        <use href="#door-shape" class="extrude-deep" x="14" y="22"/>
        <use href="#door-shape" class="extrude-deep" x="12" y="19"/>
        <use href="#door-shape" class="extrude-deep" x="10" y="16"/>
        <use href="#door-shape" class="extrude-deep" x="8" y="13"/>
        <use href="#door-shape" class="extrude-side" x="7" y="10"/>
        <use href="#door-shape" class="extrude-side" x="5" y="7"/>
        <use href="#door-shape" class="extrude-side" x="3" y="4"/>
        <use href="#door-shape" class="extrude-side" x="1" y="2"/>
      </g>
      <use href="#door-shape" class="letter-outline"/>
      <text class="block-letters letter-fill" x="236" y="362" font-size="235" textLength="735" lengthAdjust="spacingAndGlyphs"><tspan fill="url(#fill-bluff)">D</tspan><tspan fill="url(#fill-ferry)">O</tspan><tspan fill="url(#fill-barn)">O</tspan><tspan fill="url(#fill-autumn)">R</tspan></text>
      <use href="#door-shape" class="letter-edge"/>
    </g>
    <g class="word-county" transform="rotate(3 620 540)">
      <g class="extrusion">
        <use href="#county-shape" class="extrude-deep" x="14" y="22"/>
        <use href="#county-shape" class="extrude-deep" x="12" y="19"/>
        <use href="#county-shape" class="extrude-deep" x="10" y="16"/>
        <use href="#county-shape" class="extrude-deep" x="8" y="13"/>
        <use href="#county-shape" class="extrude-side" x="7" y="10"/>
        <use href="#county-shape" class="extrude-side" x="5" y="7"/>
        <use href="#county-shape" class="extrude-side" x="3" y="4"/>
        <use href="#county-shape" class="extrude-side" x="1" y="2"/>
      </g>
      <use href="#county-shape" class="letter-outline"/>
      <text class="block-letters letter-fill" x="108" y="612" font-size="230" textLength="1010" lengthAdjust="spacingAndGlyphs"><tspan fill="url(#fill-sign)">C</tspan><tspan fill="url(#fill-cherry)">O</tspan><tspan fill="url(#fill-fire)">U</tspan><tspan fill="url(#fill-shore)">N</tspan><tspan fill="url(#fill-tower)">T</tspan><tspan fill="url(#fill-lighthouse)">Y</tspan></text>
      <use href="#county-shape" class="letter-edge"/>
    </g>
  </g>

  <text class="script greeting" x="62" y="330" font-size="78" textLength="235" lengthAdjust="spacingAndGlyphs" transform="rotate(-10 160 310)">Greetings</text>
  <text class="script greeting-from" x="104" y="420" font-size="78" textLength="112" lengthAdjust="spacingAndGlyphs" transform="rotate(-10 160 410)">from</text>
  <text class="script state-name" x="512" y="702" font-size="64" textLength="232" lengthAdjust="spacingAndGlyphs" transform="rotate(-4 620 690)">Wisconsin</text>
</svg>
</body>
</html>
```